Business Card for Voltrix

Horizontal business card for voltrix, the electrical contractor.
clean and professional looking, using company branding and colours.
I also want the blue in the logo and wording to be made a more 'electric' blue and the grey 'Voltrix' to be slightly darker.

Pleas use the following contact details:

Peter Alwick
Owner

t: 01632 960581
m: 07700 900316
e: peter@voltrix-wiring.co.uk

www.voltrix-wiring.co.uk

Industry/Entity Type

Electrical

Font styles to use
Sans Serif

```html
<!DOCTYPE html>
<html lang="en">
<head>
<meta charset="utf-8">
<title>Voltrix – Business Card</title>
<link rel="stylesheet" href="https://fonts.googleapis.com/css2?family=Open+Sans:wght@400;600;700&display=swap">
<style>
  :root {
    --stage: #dcdde0;
    --card-white: #ffffff;
    --electric-blue: #0878c4;
    --electric-blue-deep: #066aad;
    --brand-grey: #55585c;
    --text-dark: #3b3d40;
    --ghost-grey: #eef0f3;
    --icon-red: #c4262e;
    --card-edge: #8a8c90;
  }
  html, body {
    margin: 0;
    width: 1200px;
    height: 1200px;
    overflow: hidden;
    background: var(--stage);
    font-family: "Open Sans", Arial, sans-serif;
  }
  .stage { position: relative; width: 1200px; height: 1200px; }

  .card {
    position: absolute;
    left: 246px;
    width: 708px;
    height: 458px;
    overflow: hidden;
    box-sizing: border-box;
  }

  /* Front */
  .card-front {
    top: 138px;
    background: var(--card-white);
    border: 1px solid var(--card-edge);
    border-radius: 0 42px 0 42px;
  }
  .front-edge-band {
    position: absolute; left: 0; top: 0; bottom: 0; width: 104px;
    background: linear-gradient(90deg, var(--electric-blue) 0%, rgba(8,120,196,0.55) 45%, rgba(255,255,255,0) 100%);
  }
  .front-ghost-word {
    position: absolute; left: -60px; top: 146px;
    font-size: 150px; font-weight: 600; letter-spacing: 34px;
    color: var(--ghost-grey); line-height: 1; white-space: nowrap;
  }
  .brand-lockup {
    position: absolute; display: flex; align-items: center; gap: 10px;
  }
  .brand-lockup .brand-dot {
    width: 34px; height: 34px; border-radius: 50%; background: var(--electric-blue);
  }
  .brand-lockup .brand-name {
    font-size: 42px; font-weight: 600; letter-spacing: 4px; color: var(--brand-grey); line-height: 1;
  }
  .card-front .brand-lockup { left: 48px; top: 44px; }

  .holder { position: absolute; left: 100px; top: 146px; }
  .holder-name { margin: 0; font-size: 24px; font-weight: 700; color: var(--electric-blue); line-height: 1.1; }
  .holder-role { margin: 2px 0 0; font-size: 18px; color: var(--text-dark); }

  .contact-list {
    position: absolute; right: 40px; top: 326px;
    margin: 0; padding: 0; list-style: none;
    font-size: 18px; color: var(--text-dark); text-align: right;
  }
  .contact-list li { display: flex; justify-content: flex-end; align-items: center; gap: 10px; height: 24px; }
  .contact-list li.gap-above { margin-top: 6px; }
  .contact-list svg { width: 18px; height: 18px; flex: none; }

  /* Back */
  .card-back {
    top: 604px;
    background: var(--electric-blue);
    border-radius: 42px 0 42px 0;
  }
  .back-ghost-disc {
    position: absolute; left: 20px; top: 40px; width: 380px; height: 380px;
    border-radius: 50%; background: rgba(255,255,255,0.09);
  }
  .card-back .brand-lockup { left: 306px; top: 282px; }
  .card-back .brand-name { color: #dfe6ec; }
  .card-back .brand-dot { background: #dfe6ec; }
  .back-web {
    position: absolute; left: 0; right: 0; bottom: 12px;
    text-align: center; font-size: 18px; color: #ffffff;
  }
</style>
</head>
<body>
<main class="stage">

  <section class="card card-front" aria-label="Business card front">
    <div class="front-edge-band"></div>
    <div class="front-ghost-word" aria-hidden="true">VOLTRIX</div>

    <div class="brand-lockup">
      <span class="brand-dot"></span>
      <span class="brand-name">VOLTRIX</span>
    </div>

    <div class="holder">
      <p class="holder-name">Peter Alwick</p>
      <p class="holder-role">Owner</p>
    </div>

    <ul class="contact-list">
      <li>01632 960581
        <svg viewBox="0 0 18 18"><path fill="var(--icon-red)" d="M4 2c1 0 2 2.5 2 3.3 0 .8-1.4 1.2-1.2 2 .5 2 2.5 4.2 4.6 4.9.8.2 1.2-1.2 2-1.2.8 0 3.3 1 3.3 2 0 1.2-1.6 2.6-3 2.6C6.6 15.6 2.4 11 2.4 5 2.4 3.6 3 2 4 2z"/></svg>
      </li>
      <li>07700 900316
        <svg viewBox="0 0 18 18"><rect x="5" y="1.5" width="8" height="15" rx="1.5" fill="var(--icon-red)"/><rect x="6.5" y="3.5" width="5" height="4.5" fill="#fff"/><g fill="#fff"><rect x="6.5" y="9.5" width="1.4" height="1.2"/><rect x="8.3" y="9.5" width="1.4" height="1.2"/><rect x="10.1" y="9.5" width="1.4" height="1.2"/><rect x="6.5" y="11.6" width="1.4" height="1.2"/><rect x="8.3" y="11.6" width="1.4" height="1.2"/><rect x="10.1" y="11.6" width="1.4" height="1.2"/></g></svg>
      </li>
      <li class="gap-above">peter@voltrix-wiring.co.uk
        <svg viewBox="0 0 18 18"><rect x="1.5" y="4" width="15" height="10" fill="var(--icon-red)"/><path d="M1.5 4l7.5 6 7.5-6M1.5 14l5.5-5M16.5 14l-5.5-5" stroke="#fff" stroke-width="1.1" fill="none"/></svg>
      </li>
      <li>www.voltrix-wiring.co.uk
        <svg viewBox="0 0 18 18"><g fill="none" stroke="var(--icon-red)" stroke-width="1.5"><circle cx="9" cy="9" r="7.2"/><ellipse cx="9" cy="9" rx="3.2" ry="7.2"/><path d="M1.8 9h14.4M3 5h12M3 13h12"/></g></svg>
      </li>
    </ul>
  </section>

  <section class="card card-back" aria-label="Business card back">
    <div class="back-ghost-disc" aria-hidden="true"></div>
    <div class="brand-lockup">
      <span class="brand-dot"></span>
      <span class="brand-name">VOLTRIX</span>
    </div>
    <p class="back-web">www.voltrix-wiring.co.uk</p>
  </section>

</main>
</body>
</html>
```